Slide Master for Halvern Engines - A Systematic Hedge Fund

We are looking for someone to produce a theme and slide master for us for our investor presentations. I have uploaded a few examples of templates that we would like to have included:
Main Title
Section Title
Slides with just bullet points
Different image/table configurations with bullet points and foot notes
Biographies of different lengths
A disclaimer (no one will read this but it should still look nice and needs to be in the presentations)
I have also uploaded the company logo, business card and colour definitions. Currently we have a blue colour scheme defined, but it would be nice to get a complementary set of colours so that when we have charts with more elements we can just draw from those.
The most important thing is that the slide master must be of general use to us. We arn't looking to have a specific presentation designed for us, but a theme/style that we can apply ourselves to any presentation we need to give in the future. It should have clearly defined guidelines for where content should go (and if this is different with and without footnotes for example). We would also like it to have a similar feel to the logo/business cards, so matt colours, high contrast, but not busy.
I'm excited to see the results!

```html
<!DOCTYPE html>
<html lang="en">
<head>
<meta charset="utf-8">
<title>Halvern Engines – Slide Master</title>
<link href="https://fonts.googleapis.com/css2?family=Roboto:wght@300;400;500;700;900&display=swap" rel="stylesheet">
<style>
  :root {
    --sheet: #e6e6e6;
    --navy: #044372;
    --navy-soft: #0d4f82;
    --sky: #5b9be0;
    --sky-pale: #eef4fb;
    --ink: #333a40;
    --rule: #c9cdd2;
    --muted: #b5b9be;
    --white: #ffffff;
  }
  * { box-sizing: border-box; margin: 0; padding: 0; }
  html, body {
    width: 1200px; height: 724px; overflow: hidden;
    background: var(--sheet);
    font-family: "Roboto", sans-serif;
  }
  .sheet { position: relative; width: 1200px; height: 724px; }

  .slide {
    position: absolute; width: 544px; height: 306px; overflow: hidden;
  }
  .slide--dark { background: var(--navy); color: var(--white); }
  .slide--light { background: var(--white); color: var(--ink); box-shadow: 0 0 0 0.5px #d6d6d6; }
  .pos-tl { left: 39px; top: 40px; }
  .pos-tr { left: 617px; top: 40px; }
  .pos-bl { left: 39px; top: 377px; }
  .pos-br { left: 617px; top: 377px; }

  /* Title slide */
  .brand {
    position: absolute; left: 59px; top: 62px;
    font-weight: 700; font-size: 11px; letter-spacing: 0.2px;
    color: var(--white); display: flex; align-items: center; gap: 5px;
  }
  .brand__dot { width: 7px; height: 7px; background: var(--sky); display: inline-block; }
  .main-title {
    position: absolute; left: 54px; top: 102px;
    font-size: 36px; line-height: 40px; font-weight: 400;
  }
  .main-date { position: absolute; left: 58px; top: 189px; font-size: 7px; }
  .hero-art {
    position: absolute; right: 0; top: 155px; width: 272px; height: 140px;
    background: linear-gradient(160deg, rgba(91,155,224,0) 20%, rgba(91,155,224,0.55) 100%);
    clip-path: polygon(0 55%, 100% 0, 100% 55%, 35% 100%, 0 75%);
  }
  .hero-art--faint {
    background: linear-gradient(160deg, rgba(91,155,224,0) 20%, rgba(91,155,224,0.2) 100%);
  }
  .hero-art--pale {
    top: 160px;
    background: linear-gradient(160deg, rgba(91,155,224,0) 20%, rgba(91,155,224,0.08) 100%);
  }
  .circulation {
    position: absolute; font-size: 4.5px; letter-spacing: 0.1px; text-transform: uppercase;
  }
  .slide--dark .circulation { right: 9px; bottom: 8px; color: var(--sky); }
  .slide--light .circulation { left: 6px; bottom: 4px; color: #6b7178; }

  /* Content slide header */
  .slide-head {
    position: absolute; top: 34px; height: 23px;
    border-bottom: 0.6px solid var(--rule);
    display: flex; justify-content: space-between; align-items: flex-end;
  }
  .slide-head--disclaimer { left: 149px; right: 30px; }
  .slide-head--sub { left: 28px; right: 30px; }
  .slide-head__title { color: var(--navy); font-size: 19px; line-height: 22px; font-weight: 300; }
  .slide-head__title strong { font-weight: 700; }
  .slide-head__title--bold { font-weight: 700; }
  .slide-head__section {
    font-size: 10px; font-weight: 300; color: var(--muted); letter-spacing: 0.2px; padding-bottom: 1px;
  }

  .network-art {
    position: absolute; left: 0; top: 150px; width: 280px; height: 142px;
    background: radial-gradient(ellipse at 10% 20%, rgba(74,110,150,0.35), rgba(180,200,225,0.12) 45%, rgba(255,255,255,0) 75%);
  }

  .disclaimer-cols {
    position: absolute; left: 149px; top: 82px; width: 339px;
    display: grid; grid-template-columns: 158px 158px; column-gap: 23px;
  }
  .disclaimer-cols p {
    font-size: 7.6px; line-height: 9.5px; font-weight: 300; text-align: justify;
    color: #2a2f34; margin-bottom: 6px; position: relative;
  }

  .footer-mark {
    position: absolute; right: 8px; bottom: 6px;
    display: flex; align-items: center; gap: 8px; font-size: 5px; color: #2a2f34;
  }
  .footer-mark__name { font-size: 3.6px; font-weight: 700; color: var(--navy); }

  /* Section slide */
  .section-title {
    position: absolute; left: 58px; top: 108px;
    font-size: 27px; font-weight: 300; line-height: 32px;
  }
  .section-title strong { font-weight: 700; }
  .section-rule { position: absolute; left: 58px; top: 147px; width: 54px; height: 2.5px; background: var(--sky); }

  /* Bullet slide */
  .col { position: absolute; top: 92px; width: 190px; }
  .col--a { left: 32px; }
  .col--b { left: 237px; }
  .col__heading { font-size: 9px; color: var(--sky); font-weight: 400; margin-bottom: 12px; }
  .col ul { list-style: none; }
  .col li {
    position: relative; padding-left: 12px; font-size: 9px; line-height: 11px;
    font-weight: 300; color: #2a2f34; margin-bottom: 5.5px;
  }
  .col li::before {
    content: ""; position: absolute; left: 1px; top: 3px;
    width: 2.5px; height: 2.5px; border-radius: 50%; background: var(--sky);
  }

  .sheet-number {
    position: absolute; right: 24px; bottom: 0; font-size: 34px; font-weight: 900; color: #9a9a9a;
    line-height: 34px;
  }
</style>
</head>
<body>
<main class="sheet">

  <section class="slide slide--dark pos-tl">
    <div class="brand"><span class="brand__dot"></span>Halvern Engines</div>
    <h1 class="main-title">Presentation<br>Tittle</h1>
    <p class="main-date">June, 2021</p>
    <div class="hero-art" role="img" aria-label="Large light-blue bridge truss decoration"></div>
    <p class="circulation">Not for circulation</p>
  </section>

  <section class="slide slide--light pos-tr">
    <div class="network-art" role="img" aria-label="Faint connected-nodes network graphic"></div>
    <header class="slide-head slide-head--disclaimer">
      <h2 class="slide-head__title slide-head__title--bold">Disclaimer</h2>
      <span class="slide-head__section">SECTION TITTLE</span>
    </header>
    <div class="disclaimer-cols">
      <div>
        <p>Lorem ipsum dolor sit amet, consectetur adipiscing elit. Vestibulum lacinia eros eu pharetra mollis. Nullam vulputate purus mi, sed maximus est sodales mollis. Mauris nec vulputate eros. Cras lectus lacus, lacinia eu dapibus ac, tincidunt eu nisi. Suspendisse in volutpat risus. Nunc pharetra porttitor lorem. Vivamus at lectus sit amet lacus dictum tincidunt at vel magna. Donec blandit nulla ac erat condimentum, fringilla feugiat ex porttitor. Proin est odio, suscipit vitae magna at, bibendum tincidunt mi. Aenean facilisis pharetra lacus sed tempus. Nam finibus eu diam eu consectetur.</p>
        <p>Lorem ipsum dolor sit amet, consectetur adipiscing elit. Vestibulum lacinia eros eu pharetra mollis. Nullam vulputate purus mi.</p>
      </div>
      <div>
        <p>Lorem ipsum dolor sit amet, consectetur adipiscing elit. Vestibulum lacinia eros eu pharetra mollis. Nullam vulputate purus mi, sed maximus est sodales mollis. Mauris nec vulputate eros. Cras lectus lacus, lacinia eu dapibus ac, tincidunt eu nisi. Suspendisse in volutpat risus. Nunc pharetra porttitor lorem. Vivamus at lectus sit amet lacus dictum tincidunt at vel magna. Donec blandit nulla ac erat condimentum, fringilla feugiat ex porttitor. Proin est odio, suscipit vitae magna at, bibendum tincidunt mi. Aenean facilisis pharetra lacus sed tempus. Nam finibus eu diam eu consectetur.</p>
        <p>Lorem ipsum dolor sit amet, consectetur adipiscing elit. Vestibulum lacinia eros eu pharetra mollis. Nullam vulputate purus mi.</p>
      </div>
    </div>
    <p class="circulation">Not for circulation</p>
    <div class="footer-mark"><span class="footer-mark__name">Halvern Engines</span><span>2</span></div>
  </section>

  <section class="slide slide--dark pos-bl">
    <div class="hero-art hero-art--faint" role="img" aria-label="Faint bridge truss background decoration"></div>
    <h2 class="section-title">Section <strong>Tittle</strong></h2>
    <div class="section-rule"></div>
  </section>

  <section class="slide slide--light pos-br">
    <div class="hero-art hero-art--pale" role="img" aria-label="Very faint bridge truss background decoration"></div>
    <header class="slide-head slide-head--sub">
      <h2 class="slide-head__title">Sub-Heading <strong>Tittle</strong></h2>
      <span class="slide-head__section">SECTION TITTLE</span>
    </header>
    <div class="col col--a">
      <h3 class="col__heading">Heading A</h3>
      <ul>
        <li>Lorem ipsum dolor sit amet, consectetura dipiscing elit</li>
        <li>Lorem ipsum dolor sit amet, consectetura dipiscing elit</li>
        <li>Lorem ipsum dolor sit amet, consectetura dipiscing elit</li>
      </ul>
    </div>
    <div class="col col--b">
      <h3 class="col__heading">Heading B</h3>
      <ul>
        <li>Lorem ipsum dolor sit amet, consectetura dipiscing elit</li>
        <li>Lorem ipsum dolor sit amet, consectetura dipiscing elit</li>
        <li>Lorem ipsum dolor sit amet, consectetura dipiscing elit</li>
      </ul>
    </div>
    <p class="circulation">Not for circulation</p>
    <div class="footer-mark"><span class="footer-mark__name">Halvern Engines</span><span>4</span></div>
  </section>

  <span class="sheet-number">1</span>
</main>
</body>
</html>
```